Cat-products company needs smart, yet endearing, business card

We need a business card design for a new, but up-and-running, business based in Honolulu, Hawaii. The business is Purrlane Nest Co. Our first product is the most environmentally-friendly cat grass kit ever seen on the planet. Future products, currently in the R&D phase, will include a variety of exciting cat scratchers. We also do consulting work to help apartment-dwellers make their home more cat-friendly and, in the future, plan on doing full, custom installs of structure to create high walkways for cats.

Target Market(s)

Middle-aged, apartment-dwelling, middle-class workers who own 1 or more cats and who dote on them.

Industry/Entity Type

Pet Care

Contact Information for Business Card

A striking, professional, yet warm and friendly design is what we're after.

Font styles to use
Serif
Sans Serif
Other font styles liked:
• Comfortaa

Colors

Designer to choose colors to be used in the design.

Requirements
Must have
• The company logo: (see attachment)
• The company name: Purrlane Nest Co
• The web address: www.purrlanenestco.example
• Email: support@purrlanenestco.example
• Phone: +1 (808) 555 0172
• Update (Fri Jun 30 3017 7:45pm Hawaii Time) I would like, is possible, uploaded picture of the cat grass kit on the back of the card with some text along the lines of: Purrlane Nest Co - Where The Freshest Kitty Sprouts Begin
Nice to have
• A cat picture, cartoon, real or silhouette that illustrates cats in action and/or relaxing; ie using the apartment space to live, play and relax in and being well-contented.
• Most of the website is done in the font: Comfortaa. It might be nice to continue using this for brand consistency.
Should not have
• Hard-to-read fonts.

```html
<!DOCTYPE html>
<html lang="en">
<head>
<meta charset="utf-8">
<title>Purrlane Nest Co – Business Card</title>
<link rel="stylesheet" href="https://fonts.googleapis.com/css2?family=Comfortaa:wght@500;700&family=Fredoka:wght@600&display=swap">
<style>
  :root {
    --backdrop: #d9d9d9;
    --brown: #5a3a34;
    --brown-deep: #4c302b;
    --yellow: #fbb617;
    --yellow-light: #fde33a;
    --yellow-deep: #f6a90f;
    --white: #ffffff;
  }
  * { box-sizing: border-box; margin: 0; padding: 0; }
  html, body {
    width: 1200px; height: 750px; overflow: hidden;
    background: var(--backdrop);
  }
  .sheet {
    width: 1200px; height: 750px;
    display: flex; align-items: center; justify-content: center; gap: 40px;
  }
  .card {
    position: relative;
    width: 540px; height: 309px;
    border-radius: 34px;
    overflow: hidden;
    box-shadow: 0 6px 18px rgba(0,0,0,0.18);
  }

  /* Contact side */
  .card--contact { background: linear-gradient(110deg, var(--brown-deep), var(--brown)); }
  .contact__panel {
    position: absolute; top: 0; right: 0; bottom: 0; width: 120px;
    background: var(--yellow);
    clip-path: polygon(45% 0, 100% 0, 100% 100%, 0 100%, 0 40%);
  }
  .contact__body {
    position: absolute; left: 70px; top: 0; bottom: 0; width: 330px;
    display: flex; flex-direction: column; justify-content: center; align-items: center;
  }
  .brand-name {
    font-family: "Fredoka", sans-serif; font-weight: 600;
    letter-spacing: 0.5px; line-height: 1; white-space: nowrap;
  }
  .contact__name { color: var(--yellow); font-size: 30px; margin-bottom: 26px; }
  .contact__list { list-style: none; }
  .contact__item {
    display: flex; align-items: center; gap: 10px;
    font-family: "Comfortaa", sans-serif; font-weight: 700;
    font-size: 13px; color: var(--white); margin-bottom: 10px;
    white-space: nowrap;
  }
  .contact__item:last-child { margin-bottom: 0; }
  .contact__item--web { color: var(--yellow); }
  .contact__icon { width: 18px; height: 18px; flex: none; }

  /* Brand side */
  .card--brand {
    background: radial-gradient(circle at 68% 18%, var(--yellow-light) 0%, var(--yellow) 45%, var(--yellow-deep) 100%);
  }
  .brand__photo {
    position: absolute; left: 130px; top: 170px; width: 260px; height: 139px;
    background: radial-gradient(ellipse at 50% 60%, rgba(240,150,20,0.55), rgba(251,182,23,0) 70%);
  }
  .brand__mark {
    position: absolute; left: 0; right: 0; top: 118px;
    display: flex; align-items: center; justify-content: center; gap: 14px;
  }
  .brand__dot { width: 22px; height: 22px; border-radius: 50%; background: var(--brown); flex: none; }
  .brand__name { color: var(--white); font-size: 42px; }
</style>
</head>
<body>
  <main class="sheet">
    <section class="card card--contact" aria-label="Card back with contact details">
      <div class="contact__panel"></div>
      <div class="contact__body">
        <p class="brand-name contact__name">Purrlane Nest Co</p>
        <ul class="contact__list">
          <li class="contact__item">
            <svg class="contact__icon" viewBox="0 0 24 24" aria-hidden="true"><path fill="#fff" d="M6.6 10.8a15.1 15.1 0 0 0 6.6 6.6l2.2-2.2a1 1 0 0 1 1-.25 11.4 11.4 0 0 0 3.6.57 1 1 0 0 1 1 1V20a1 1 0 0 1-1 1A17 17 0 0 1 3 4a1 1 0 0 1 1-1h3.5a1 1 0 0 1 1 1c0 1.25.2 2.45.57 3.57a1 1 0 0 1-.25 1z"/></svg>
            +1 (808) 555 0172
          </li>
          <li class="contact__item">
            <svg class="contact__icon" viewBox="0 0 24 24" aria-hidden="true"><rect x="2" y="5" width="20" height="14" rx="1.5" fill="#fff"/><path d="M3 6l9 7 9-7" fill="none" stroke="#5a3a34" stroke-width="1.6"/></svg>
            support@purrlanenestco.example
          </li>
          <li class="contact__item contact__item--web">
            <svg class="contact__icon" viewBox="0 0 24 24" aria-hidden="true"><circle cx="12" cy="12" r="9.5" fill="none" stroke="#fbb617" stroke-width="2"/><ellipse cx="12" cy="12" rx="4" ry="9.5" fill="none" stroke="#fbb617" stroke-width="1.6"/><path d="M2.5 12h19" stroke="#fbb617" stroke-width="1.6"/></svg>
            www.purrlanenestco.example
          </li>
        </ul>
      </div>
    </section>

    <section class="card card--brand" aria-label="Card front with company name">
      <div class="brand__photo" role="img" aria-label="Faint photo of a relaxed ginger cat lying down"></div>
      <div class="brand__mark">
        <span class="brand__dot"></span>
        <p class="brand-name brand__name">Purrlane Nest Co</p>
      </div>
    </section>
  </main>
</body>
</html>
```